Packaging Design Project Screen Protector

Hi

Looking for mobile phone screen protector design. Layout is attached.

Also need Logo for this brand. So we need Logo and Package design.

H:18,5cm
W:10cm

Logo name: VOLTAN

```html
<!DOCTYPE html>
<html lang="en">
<head>
<meta charset="utf-8">
<title>VOLTAN Screen Protector Packaging</title>
<link rel="stylesheet" href="https://fonts.googleapis.com/css2?family=Roboto+Condensed:wght@400;500;700&family=Arimo:wght@400;700&display=swap">
<style>
  :root {
    --page: #ffffff;
    --card: #fbfbfb;
    --ink: #2b2b2b;
    --grey: #7b7b7b;
    --label: #555555;
    --teal: #1b8fb0;
    --blue: #1e9ad6;
    --green: #7a9a48;
    --yellow: #f5c400;
    --orange: #e8621e;
  }
  * { margin: 0; padding: 0; box-sizing: border-box; }
  html, body { width: 1200px; height: 1000px; overflow: hidden; background: var(--page); }
  .canvas { position: relative; width: 1200px; height: 1000px; }

  .pack {
    position: absolute; top: 38px; width: 522px; height: 927px;
    background: var(--card); overflow: hidden;
    box-shadow: 0 2px 8px rgba(0,0,0,.25);
  }
  .pack--front { left: 46px; }
  .pack--back { left: 636px; width: 519px; }
  .pack__art { position: absolute; inset: 0; width: 100%; height: 100%; }

  .brand {
    position: absolute; left: 42px; top: 50px;
    font: 700 24px/1 "Roboto Condensed", sans-serif; letter-spacing: 1px; color: var(--grey);
  }
  .headline { position: absolute; left: 0; right: 0; top: 130px; text-align: center; font-family: "Roboto Condensed", sans-serif; }
  .headline__top { font-size: 38px; line-height: 42px; font-weight: 500; color: #3a3a3a; }
  .headline__main { font-size: 50px; line-height: 54px; font-weight: 500; color: var(--teal); }
  .headline__sub { font-size: 32px; line-height: 38px; font-weight: 500; color: #333; }
  .product-visual {
    position: absolute; left: 24px; top: 262px; width: 476px; height: 320px;
    background: linear-gradient(160deg, #f2f2f2 0%, #e6e6e6 60%, #f4f4f4 100%);
    border-radius: 30px;
  }

  .badge {
    position: absolute; border-radius: 50%;
    transform: translate(-50%, -50%);
  }
  .badge--green { background: radial-gradient(circle at 40% 35%, #9bb86a, var(--green)); }
  .badge--blue { background: radial-gradient(circle at 40% 35%, #5cc0ee, var(--blue)); }
  .badge--yellow { background: radial-gradient(circle at 40% 35%, #ffe45a, var(--yellow)); }
  .badge--orange { background: radial-gradient(circle at 40% 35%, #f59a5c, var(--orange)); }
  .badge-label {
    position: absolute; transform: translateX(-50%); white-space: nowrap;
    font: 400 15px/1 "Roboto Condensed", sans-serif; letter-spacing: .5px; color: var(--label);
  }
  .badge-label--small { font-size: 12px; }

  .features-tab {
    position: absolute; left: 0; top: 87px; width: 236px; height: 35px;
    background: var(--blue); color: #fff;
    font: 400 28px/35px "Roboto Condensed", sans-serif; padding-left: 52px;
  }
  .feature {
    position: absolute;
    font: 700 18px/25px "Arimo", sans-serif; color: var(--grey);
  }
  .feature::before {
    content: ""; position: absolute; left: -20px; top: 6px;
    width: 5px; height: 5px; border-radius: 50%; background: var(--yellow);
  }
  .intro-title {
    position: absolute; left: 54px; top: 380px;
    font: 700 20px/26px "Arimo", sans-serif; color: var(--blue);
  }
  .steps { position: absolute; left: 54px; top: 424px; width: 200px; list-style: none; }
  .steps li { font: 400 14px/20px "Arimo", sans-serif; color: var(--grey); margin-bottom: 20px; }
  .steps b { color: var(--blue); }
  .device-visual {
    position: absolute; left: 56px; top: 749px; width: 60px; height: 125px;
    border-radius: 8px; background: linear-gradient(160deg, #3a3a3a, #111);
  }
  .origin { position: absolute; left: 147px; top: 797px; font: 400 11px/16px "Arimo", sans-serif; color: var(--grey); }
  .trademark { position: absolute; left: 54px; top: 891px; font: 700 10.5px/14px "Arimo", sans-serif; color: var(--grey); }
</style>
</head>
<body>
<div class="canvas">
  <svg width="0" height="0" style="position:absolute">
    <defs>
      <radialGradient id="glow-yellow" cx="0" cy="0" r="1">
        <stop offset="0" stop-color="#fff29a"/>
        <stop offset="1" stop-color="#fff29a" stop-opacity="0"/>
      </radialGradient>
    </defs>
  </svg>

  <section class="pack pack--front">
    <svg class="pack__art" viewBox="0 0 522 927">
      <ellipse cx="0" cy="0" rx="260" ry="160" fill="url(#glow-yellow)"/>
      <ellipse cx="80" cy="927" rx="420" ry="200" fill="url(#glow-yellow)"/>
      <path d="M 150 0 Q 430 10 522 180 L 522 150 Q 440 20 200 0 Z" fill="#cfcfcf"/>
      <path d="M 0 700 Q 200 560 522 580 L 522 600 Q 260 590 0 740 Z" fill="#d6d6d6"/>
      <path d="M 0 740 Q 260 590 522 600 L 522 927 L 0 927 Z" fill="#ffffff" opacity=".6"/>
    </svg>

    <div class="brand">VOLTAN</div>
    <div class="headline">
      <div class="headline__top">HIGH QUALITY</div>
      <div class="headline__main">SCREEN PROTECTOR</div>
      <div class="headline__sub">FOR SMARTPHONES</div>
    </div>
    <div class="product-visual" role="img" aria-label="Line drawing of a smartphone with a screen protector film peeling off its display"></div>

    <div class="badge badge--green" style="left:212px; top:697px; width:96px; height:96px;" role="img" aria-label="Scratch resistance badge icon"></div>
    <div class="badge-label" style="left:212px; top:752px;">Againts Scratches</div>
    <div class="badge badge--blue" style="left:397px; top:680px; width:112px; height:112px;" role="img" aria-label="Clear vision badge icon"></div>
    <div class="badge-label" style="left:397px; top:743px;">Clear Vision</div>
    <div class="badge badge--yellow" style="left:97px; top:830px; width:120px; height:120px;" role="img" aria-label="Reusable badge icon"></div>
    <div class="badge-label" style="left:97px; top:897px; font-size:17px;">Reausable</div>
    <div class="badge badge--orange" style="left:304px; top:816px; width:96px; height:96px;" role="img" aria-label="Smooth touch badge icon"></div>
    <div class="badge-label" style="left:304px; top:870px;">Smooth Touch Feeling</div>
  </section>

  <section class="pack pack--back">
    <svg class="pack__art" viewBox="0 0 519 927">
      <ellipse cx="0" cy="0" rx="240" ry="150" fill="url(#glow-yellow)"/>
      <path d="M 290 0 Q 470 30 519 130 L 519 100 Q 460 20 340 0 Z" fill="#cfcfcf"/>
      <path d="M 60 336 Q 320 330 519 400 L 519 370 Q 320 320 60 336 Z" fill="#d2d2d2"/>
      <path d="M 0 760 Q 250 740 519 650 L 519 675 Q 260 760 0 775 Z" fill="#d6d6d6"/>
      <ellipse cx="120" cy="927" rx="380" ry="150" fill="url(#glow-yellow)" opacity=".5"/>
    </svg>

    <div class="features-tab">Features:</div>
    <div class="feature" style="left:79px; top:144px; width:160px;">Protects Screen from Scratches</div>
    <div class="feature" style="left:79px; top:220px;">Resist Fingerprints</div>
    <div class="feature" style="left:81px; top:270px;">Eco-Friendly</div>
    <div class="feature" style="left:274px; top:144px;">Easy Installation</div>
    <div class="feature" style="left:274px; top:195px; width:130px;">Residue-Free Removal</div>
    <div class="feature" style="left:274px; top:270px;">Precision Cut &amp; Fit</div>

    <div class="intro-title">Introduction:</div>
    <ol class="steps">
      <li><b>1.</b> Clean mobile phone screen protector on mobile phone</li>
      <li><b>2.</b> Peel red label and apply screen protector on mobile phone</li>
      <li><b>3.</b> Swipe air bubbles to the edge and remove them from the screen</li>
      <li><b>4.</b> Remove the blue label after application is done</li>
    </ol>

    <div class="badge badge--orange" style="left:380px; top:438px; width:74px; height:74px;" role="img" aria-label="Smooth touch badge icon"></div>
    <div class="badge-label badge-label--small" style="left:380px; top:480px;">Smooth Touch Feeling</div>
    <div class="badge badge--green" style="left:319px; top:542px; width:74px; height:74px;" role="img" aria-label="Scratch resistance badge icon"></div>
    <div class="badge-label badge-label--small" style="left:319px; top:584px;">Againts Scratches</div>
    <div class="badge badge--blue" style="left:454px; top:542px; width:74px; height:74px;" role="img" aria-label="Clear vision badge icon"></div>
    <div class="badge-label badge-label--small" style="left:454px; top:584px;">Clear Vision</div>
    <div class="badge badge--yellow" style="left:386px; top:640px; width:74px; height:74px;" role="img" aria-label="Reusable badge icon"></div>
    <div class="badge-label badge-label--small" style="left:386px; top:682px;">Reausable</div>

    <div class="device-visual" role="img" aria-label="Small smartphone with a protector film lifting from its screen"></div>
    <div class="origin">Made in Turkey<br>Designed in Istanbul<br>Material in Japan</div>
    <div class="trademark">VOLTAN brand and its logo registered trademark of KORAY TEKNIK ELEKTRONIK</div>
  </section>
</div>
</body>
</html>
```